Real Estate Sales Brokerage

Design a modern and fresh looking standard size business card, incorporate our logo's color scheme and modern appearance with head shot photo on front side and incorporate our log on the back side

Target Market(s)

Residential Home sales

Industry/Entity Type

Real Estate Agent

Font styles to use
Sans Serif

Colors

Designer to choose colors to be used in the design.

Requirements
Must have
• fresh, modern, not too busy, incorporate head shot in front of the card, incorporate logo in front and back of the card. Use logo design scheme as appropriate.
Nice to have
• horizontal and vertical options to compare would be nice.

```html
<!DOCTYPE html>
<html lang="en">
<head>
<meta charset="utf-8">
<title>Harborline Home Realty – Business Card</title>
<link rel="stylesheet" href="https://fonts.googleapis.com/css2?family=Roboto:wght@400;500;700&display=swap">
<style>
  :root {
    --olive: #5f5c36;
    --yellow: #f4d34a;
    --white: #ffffff;
    --backdrop: #d2d2d2;
    --photo-top: #e6e8ee;
    --photo-mid: #3a5488;
    --photo-bottom: #22386a;
  }
  * { margin: 0; padding: 0; box-sizing: border-box; }
  html, body { width: 900px; height: 1200px; overflow: hidden; }
  body {
    background: var(--backdrop);
    font-family: "Roboto", Arial, sans-serif;
    position: relative;
  }
  .card {
    position: absolute;
    left: 85px;
    width: 733px;
    height: 429px;
    border-radius: 22px;
    overflow: hidden;
  }
  .card--front { top: 138px; background: var(--white); }
  .card--back { top: 633px; background: var(--olive); }
  .card__art { position: absolute; inset: 0; }

  .brand {
    position: absolute;
    display: flex;
    align-items: center;
    gap: 14px;
  }
  .brand__mark { width: 34px; height: 34px; flex: none; }
  .brand__name {
    font-weight: 500;
    font-size: 31px;
    line-height: 1.05;
    text-transform: uppercase;
  }
  .card--front .brand { left: 42px; top: 58px; }
  .card--front .brand__mark { background: var(--olive); }
  .card--front .brand__name { color: var(--olive); }
  .card--back .brand { left: 183px; top: 150px; }
  .card--back .brand__mark { background: var(--white); }
  .card--back .brand__name { color: var(--white); }

  .agent { position: absolute; left: 63px; top: 204px; }
  .agent__name { color: var(--olive); font-weight: 700; font-size: 21px; letter-spacing: .3px; }
  .agent__title { color: var(--yellow); font-size: 14.5px; margin-top: 5px; text-transform: uppercase; }

  .contact {
    position: absolute;
    left: 63px;
    top: 281px;
    list-style: none;
    color: var(--white);
    font-size: 15px;
    line-height: 22px;
  }
  .contact__item { display: flex; gap: 9px; }
  .contact__item + .contact__item { margin-top: 1px; }
  .contact__item--address + .contact__item { margin-top: 8px; }
  .contact__icon {
    flex: none;
    width: 18px; height: 18px;
    margin-top: 2px;
    border-radius: 4px;
    background: var(--yellow);
  }
  .contact__icon svg { display: block; width: 18px; height: 18px; }

  .headshot {
    position: absolute;
    left: 440px;
    top: 8px;
    width: 293px;
    height: 421px;
    background: linear-gradient(180deg, var(--photo-top) 0%, var(--photo-mid) 45%, var(--photo-bottom) 100%);
  }
  .stripe {
    position: absolute;
    left: 680px;
    top: 0;
    width: 22px;
    height: 429px;
    background: var(--yellow);
  }
</style>
</head>
<body>

<section class="card card--front" aria-label="Business card front">
  <svg class="card__art" viewBox="0 0 733 429" aria-hidden="true">
    <path d="M0,262 C150,258 330,240 450,205 C560,170 680,80 733,18 L733,429 L0,429 Z" fill="var(--olive)"/>
    <path d="M280,429 C470,390 640,270 733,28 L733,70 C660,290 500,400 330,429 Z" fill="var(--white)"/>
    <path d="M330,429 C500,400 660,290 733,70 L733,170 C680,320 560,410 440,429 Z" fill="var(--yellow)"/>
  </svg>

  <div class="brand">
    <span class="brand__mark"></span>
    <span class="brand__name">Harborline<br>Home<br>Realty</span>
  </div>

  <div class="agent">
    <p class="agent__name">DANIEL MERCER</p>
    <p class="agent__title">Managing Director</p>
  </div>

  <ul class="contact">
    <li class="contact__item contact__item--address">
      <span class="contact__icon"><svg viewBox="0 0 18 18"><path d="M9 3.5a3.6 3.6 0 0 0-3.6 3.6c0 2.7 3.6 7 3.6 7s3.6-4.3 3.6-7A3.6 3.6 0 0 0 9 3.5zm0 5a1.4 1.4 0 1 1 0-2.8 1.4 1.4 0 0 1 0 2.8z" fill="var(--olive)"/></svg></span>
      <span>418 W. Lindenway<br>Suite 920, P.O. Box 41086</span>
    </li>
    <li class="contact__item">
      <span class="contact__icon"><svg viewBox="0 0 18 18"><rect x="5.5" y="3" width="7" height="12" rx="1.2" fill="var(--olive)"/><rect x="6.8" y="4.6" width="4.4" height="7.4" fill="var(--yellow)"/></svg></span>
      <span>555.204.6187</span>
    </li>
    <li class="contact__item">
      <span class="contact__icon"><svg viewBox="0 0 18 18"><rect x="3.5" y="5" width="11" height="8" rx="1" fill="none" stroke="var(--olive)" stroke-width="1.5"/><path d="M3.8 5.5 9 9.6l5.2-4.1" fill="none" stroke="var(--olive)" stroke-width="1.5"/></svg></span>
      <span>dan@harborlinehomerealty.com</span>
    </li>
    <li class="contact__item">
      <span class="contact__icon"><svg viewBox="0 0 18 18"><circle cx="9" cy="9" r="5.2" fill="none" stroke="var(--olive)" stroke-width="1.5"/><path d="M3.8 9h10.4M9 3.8c-2.4 2.8-2.4 7.6 0 10.4M9 3.8c2.4 2.8 2.4 7.6 0 10.4" fill="none" stroke="var(--olive)" stroke-width="1.1"/></svg></span>
      <span>www.harborlinehomerealty.com</span>
    </li>
  </ul>

  <div class="headshot" role="img" aria-label="Headshot photo of the managing director in a navy suit"></div>
</section>

<section class="card card--back" aria-label="Business card back">
  <div class="stripe"></div>
  <div class="brand">
    <span class="brand__mark"></span>
    <span class="brand__name">Harborline<br>Home<br>Realty</span>
  </div>
</section>

</body>
</html>
```